Honey Company from Florida Needs Sweet and Buzz-worthy Site

Website Requests:
-Deluxe 5-Page Website with SSL-Secure Online Store (Shopify)
-High-end imagery to appeal to a discerning consumer
-Detailed verbiage with strong SEO and easy readability
-Design principles: simple, chic, luxe, earthy
Pages:
1. Home {Local, Raw American Honey from Florida}
2. The Hive
> About Us
>Meet the Beekeepers
3. Buy Honey
> Shopify retail store
4. The Buzz {News, Recipes & More}
> Blog
5. Contact Us {We're Buzzin' to Meet You}
> Store Hours
> Phone Number
> Address
> Quick Contact Form
Target Market(s)
High-end honey consumer in the U.S.
Industry/Entity Type
Upscale honey enthusiasts; direct to consumer sales.
Coding
Coded - Design and coding required
Number of Pages Required
5+ page
Requirements
Must have
- Upscale look and feel, easy usability for quick sales.

```html
<!DOCTYPE html>
<html lang="en">
<head>
<meta charset="utf-8">
<title>Golden Comb Company — Raw Florida Honey</title>
<link href="https://fonts.googleapis.com/css2?family=Bitter:wght@400;700&family=Noticia+Text:wght@400;700&display=swap" rel="stylesheet">
<style>
:root{
  --honey:#f0c75a;
  --honey-text:#e8c055;
  --ink:#1c1c1c;
  --body:#2a2a2a;
  --rule:#e6e6e6;
  --card:#f0f0f0;
  --white:#ffffff;
}
*{margin:0;padding:0;box-sizing:border-box}
html,body{width:1200px;height:3197px;overflow:hidden;background:var(--white)}
body{position:relative;font-family:"Noticia Text",Georgia,serif;color:var(--body)}
.abs{position:absolute}
.center{text-align:center}
.heading{font-family:"Bitter",Georgia,serif;font-weight:700;color:var(--ink);letter-spacing:.5px;text-transform:uppercase}
.subheading{font-family:"Bitter",Georgia,serif;font-weight:700;color:var(--honey-text);font-size:17px}
.copy{font-size:14.5px;line-height:25.7px;color:var(--body)}
.btn{display:flex;align-items:center;justify-content:center;background:var(--honey);font-family:"Bitter",Georgia,serif;font-weight:700;font-size:15px;color:var(--ink);text-transform:uppercase}
.rule{height:1px;background:var(--rule);left:112px;width:976px}

.announcement{left:0;top:0;width:1200px;height:42px;background:var(--honey);font-size:12px;color:var(--ink);display:flex;align-items:center;justify-content:center}
.search{left:112px;top:76px;width:124px;height:36px;border-bottom:1px solid #cfcfcf;display:flex;align-items:center;gap:12px;font-size:14px;color:var(--ink)}
.brand{left:556px;top:50px;width:88px;height:88px;border-radius:50%;border:2px solid var(--ink);display:flex;align-items:center;justify-content:center;font-family:"Bitter",serif;font-weight:700;font-size:12px;line-height:14px;text-align:center;color:var(--ink)}
.header-icons{left:1010px;top:70px;display:flex;gap:24px}
.main-nav{left:0;top:180px;width:1200px;display:flex;justify-content:center;gap:44px;font-size:14.5px;color:var(--ink)}

.hero{left:0;top:248px;width:1200px;height:514px;background:radial-gradient(ellipse at 50% 55%,#6a5326 0%,#4a3a1c 55%,#2e2514 100%)}
.hero-title{left:0;top:415px;width:1200px;font-family:"Bitter",serif;font-weight:700;font-size:52px;color:var(--white);letter-spacing:1px}
.hero-tagline{left:0;top:489px;width:1200px;font-size:12.5px;color:var(--white)}
.play{left:576px;top:533px;width:48px;height:48px;border-radius:50%;background:var(--white);display:flex;align-items:center;justify-content:center}

.product-card{top:1231px;width:309px;height:292px;background:var(--card)}
.product-card .photo{position:absolute;left:60px;top:40px;width:189px;height:180px;border-radius:6px}
.product-card.is-active{background:var(--white);box-shadow:0 1px 6px rgba(0,0,0,.22)}
.quick-shop{left:22px;top:241px;width:265px;height:41px}
.product-name{top:1540px;width:309px;font-size:29px;color:var(--ink)}
.product-price{top:1589px;width:309px;font-size:13px;color:var(--honey-text)}

.photo-block{border-radius:0}
.newsletter-input{left:406px;top:2828px;width:239px;height:47px;border:1px solid #cfcfcf;font-size:12px;color:#9a9a9a;display:flex;align-items:center;padding-left:14px}
.contact-row{left:116px;top:2986px;display:flex;align-items:center;gap:10px;font-size:13.5px;color:var(--ink)}
.socials{left:632px;top:2988px;display:flex;gap:16px}
.socials span{width:14px;height:14px;border-radius:50%;background:var(--ink)}
.footer-nav{left:113px;top:3086px;display:flex;gap:44px;font-size:14.5px;color:var(--ink)}
.legal{left:112px;top:3130px;font-size:14px;color:var(--ink)}
</style>
</head>
<body>

<div class="abs announcement">He says that 100 percent raw honey has health benefits</div>

<div class="abs search">
  <svg width="20" height="20" viewBox="0 0 20 20"><circle cx="8" cy="8" r="6" fill="none" stroke="#1c1c1c" stroke-width="2.6"/><line x1="12.5" y1="12.5" x2="18" y2="18" stroke="#1c1c1c" stroke-width="2.8" stroke-linecap="round"/></svg>
  <span>Search</span>
</div>

<div class="abs brand">GOLDEN<br>COMB<br>COMPANY</div>

<div class="abs header-icons">
  <svg width="28" height="28" viewBox="0 0 28 28" aria-label="Account"><circle cx="14" cy="14" r="12" fill="none" stroke="#1c1c1c" stroke-width="2"/><circle cx="14" cy="11" r="4.5" fill="#1c1c1c"/><path d="M6 22c2-4 5-5.5 8-5.5s6 1.5 8 5.5" fill="#1c1c1c"/></svg>
  <svg width="28" height="28" viewBox="0 0 28 28" aria-label="Cart"><path d="M2 5h4l3 13h14l3-10H8" fill="none" stroke="#1c1c1c" stroke-width="2" stroke-linejoin="round"/><circle cx="11" cy="23" r="2" fill="#1c1c1c"/><circle cx="21" cy="23" r="2" fill="#1c1c1c"/></svg>
</div>

<nav class="abs main-nav"><span>Home</span><span>The Hive</span><span>Buy Honey</span><span>The Buzz</span><span>Contact</span></nav>
<div class="abs rule" style="top:215px"></div>

<section>
  <div class="abs hero" role="img" aria-label="Honeybees crawling over golden honeycomb"></div>
  <h1 class="abs hero-title center">GOLDEN COMB</h1>
  <p class="abs hero-tagline center">“Blessed to Bee-keep” “Straight from our beloved hives to your lovely home”</p>
  <div class="abs play"><svg width="14" height="16" viewBox="0 0 14 16"><path d="M3 2l9 6-9 6z" fill="#1c1c1c"/></svg></div>
</section>

<section>
  <h2 class="abs heading center" style="left:0;top:845px;width:1200px;font-size:24px">Bee Removals</h2>
  <p class="abs copy center" style="left:180px;top:910px;width:840px">100% raw, unfiltered Florida honey straight from he beehives on his six-acre property, Golden Comb Honey Farm, 4180 Orchard Lane in Clermont. Agricultural Company specializing in the Production of 100% Raw American Honey, and the Pollination of America’s food crops. Our Honey comes straight from our beehives to your table. No filtering, heating, or any funny stuff. Just All Natural, 100% Pure Florida Honey Natural Wild Honey- flavors include Orange Blossom, Gallberry, Summer Wildflower, Winter Wildflower, and many more. Bee Pollen, Royal Jelly, and Bee venom. Bee removals are done by Dale Morrow, owner of Golden Comb Honey Farm, has about 1,200 beehives that he moves around to pollinate different plants.</p>
  <div class="abs btn" style="left:533px;top:1098px;width:134px;height:46px">Learn More</div>
</section>

<section>
  <div class="abs product-card is-active" style="left:112px">
    <div class="photo" role="img" aria-label="Hexagonal honey jars in amber and cream packaging" style="background:linear-gradient(135deg,#d9a556,#8a5a2a)"></div>
    <div class="abs btn quick-shop">Quick Shop</div>
  </div>
  <div class="abs product-card" style="left:446px">
    <div class="photo" role="img" aria-label="Honey jar beside an open gift box" style="background:linear-gradient(135deg,#e8dcc0,#c7a765)"></div>
  </div>
  <div class="abs product-card" style="left:779px">
    <div class="photo" role="img" aria-label="Gift box set of three honey jars with dipper" style="background:linear-gradient(180deg,#c9a56a,#7a4e1e)"></div>
  </div>
  <div class="abs product-name center" style="left:112px">Wild Bloom</div>
  <div class="abs product-name center" style="left:446px">Orange Grove</div>
  <div class="abs product-name center" style="left:779px">Amber Trio</div>
  <div class="abs product-price center" style="left:112px">$52.00</div>
  <div class="abs product-price center" style="left:446px">$52.00</div>
  <div class="abs product-price center" style="left:779px">$52.00</div>
</section>

<section>
  <h2 class="abs heading center" style="left:112px;top:1754px;width:466px;font-size:26px">Importance of Bees</h2>
  <p class="abs subheading center" style="left:112px;top:1800px;width:466px">Don’t Judge a Bee by Its Stinger</p>
  <p class="abs copy center" style="left:130px;top:1836px;width:430px">If the bee disappeared off the face of the Earth, man would have only four years left to live. Hyper-efficient insects do play a vital role in agriculture. Almonds, for example, are almost entirely dependent on honeybee pollination.</p>
  <div class="abs btn" style="left:278px;top:1961px;width:135px;height:46px">Learn More</div>
  <div class="abs photo-block" role="img" aria-label="Close-up of a honeybee on amber honeycomb" style="left:600px;top:1690px;width:488px;height:387px;background:radial-gradient(ellipse at 70% 45%,#c98a2e 0%,#a5621a 50%,#6e3a0c 100%)"></div>
</section>

<div class="abs rule" style="top:2146px"></div>

<section>
  <div class="abs photo-block" role="img" aria-label="Honey dripping over glowing honeycomb cells" style="left:112px;top:2214px;width:488px;height:386px;background:radial-gradient(ellipse at 50% 40%,#f0a02a 0%,#d56d10 55%,#9a3e06 100%)"></div>
  <h2 class="abs heading center" style="left:622px;top:2267px;width:464px;font-size:26px">The Health Benefits of Honey</h2>
  <p class="abs subheading center" style="left:622px;top:2312px;width:464px">Real Local Honey, Really Good for You</p>
  <p class="abs copy center" style="left:648px;top:2350px;width:412px">Raw honey is loaded with antioxidants to protect your body from cell damage due to free radicals. Honey has been long known as a folk remedy to help heal burns and wounds due to its antibacterial and antifungal properties. Honey is also very well known to soothe a sore throat.</p>
  <div class="abs btn" style="left:788px;top:2494px;width:135px;height:46px">Learn More</div>
</section>

<div class="abs rule" style="top:2687px"></div>

<section>
  <h2 class="abs heading center" style="left:0;top:2718px;width:1200px;font-size:26px">Join Our Newsletter</h2>
  <p class="abs center" style="left:0;top:2765px;width:1200px;font-size:14.5px;color:var(--ink)">Sign up today to receive updates on new arrivals and exclusive deals.</p>
  <div class="abs newsletter-input">Email Address</div>
  <div class="abs btn" style="left:658px;top:2828px;width:134px;height:47px">Subscribe</div>
</section>

<div class="abs rule" style="top:2962px"></div>

<footer>
  <div class="abs contact-row">
    <svg width="13" height="13" viewBox="0 0 24 24"><path d="M6.6 10.8a15 15 0 0 0 6.6 6.6l2.2-2.2c.3-.3.7-.4 1-.2 1.1.4 2.3.6 3.6.6.6 0 1 .4 1 1V20c0 .6-.4 1-1 1A17 17 0 0 1 3 4c0-.6.4-1 1-1h3.5c.6 0 1 .4 1 1 0 1.3.2 2.5.6 3.6.1.3 0 .7-.2 1z" fill="#1c1c1c"/></svg>
    <span>(352) 555-0172</span>
    <svg width="11" height="14" viewBox="0 0 12 16" style="margin-left:6px"><path d="M6 0a6 6 0 0 0-6 6c0 4.5 6 10 6 10s6-5.5 6-10a6 6 0 0 0-6-6z" fill="#1c1c1c"/><circle cx="6" cy="6" r="2.2" fill="#fff"/></svg>
    <span>4180 Orchard Lane, Clermont, FL 34711</span>
  </div>
  <div class="abs socials" aria-label="Social links"><span></span><span></span><span></span><span></span></div>
  <nav class="abs footer-nav"><span>Home</span><span>The Hive</span><span>Buy Honey</span><span>The Buzz</span><span>Contact</span></nav>
  <p class="abs legal">©Copyrights 2021 Company Name &nbsp; | &nbsp; All Rights Reserved</p>
</footer>

</body>
</html>
```